starlitmanesandtails pet therapy animals

I would like a business card to genarate posative emotions within people. My program has been running in a retirement village for over 5 years I work with residents and family members. My dogs work in palative care and are a great support to family members at the end stage. I also support the families and friends at furnerals when needed to dogs are always with me. Starlitmanes started with the death of my first therapy dog Milo there was such an out cry of grief within the town and retirement village that he had his own furneral The hooves came into it when I was donated a beautiful Miniature horse for the pet therapy program with great results. I now need something very special as a business card. Eg Angelwings my dogs are King Charles Cavaliers so with what I have described can you create something beautiful to acknowledge to work I do and promote it more.

Reason: The reason I have extended the deadline to give other designers a chance to look at the job. So far I have 3 designs. I am hoping to get a few more.

Industry/Entity Type

Town

Contact Information for Business Card

Starlitmanesandtails pet therapy animals
Rosalind Varga
E-mail starlitmanesandtails@quellnet.com
Mobile 0417650382
Pet therapy animals give unconditional love to the aged and disabled.

Font styles to use
Decorative

Colors

Designer to choose colors to be used in the design.

Requirements
Nice to have
• angelwings a King Charles Cavalier tan and white with angel wings and a horse with angel wings

```html
<!DOCTYPE html>
<html lang="en">
<head>
<meta charset="utf-8">
<title>Starlitmanesandtails – Business Card</title>
<link rel="stylesheet" href="https://fonts.googleapis.com/css2?family=Cinzel:wght@400;600&family=Arimo:wght@400;700&display=swap">
<style>
  :root {
    --backdrop: #e8e5e0;
    --card-white: #ffffff;
    --card-blue: #535aa8;
    --ink-violet: #5457a0;
    --art-pink: #d9a8d6;
    --art-lilac: #8f8fd0;
    --art-tan: #b8773f;
    --text-white: #ffffff;
    --text-soft: #d9dbf2;
    --rule-soft: #8d92c9;
  }
  * { box-sizing: border-box; margin: 0; padding: 0; }
  html, body {
    width: 1200px; height: 581px; overflow: hidden;
    background: var(--backdrop);
  }
  .card {
    position: absolute; left: 127px; top: 145px;
    width: 946px; height: 291px;
    display: flex;
  }
  .card-front {
    width: 473px; height: 100%;
    background: var(--card-white);
    position: relative;
  }
  .card-back {
    width: 473px; height: 100%;
    background: var(--card-blue);
    position: relative;
    color: var(--text-white);
  }
  .mascot-art {
    position: absolute; left: 135px; top: 20px;
    width: 200px; height: 185px;
    border-radius: 50% 50% 12px 12px;
    background: linear-gradient(135deg, var(--art-pink) 0%, var(--art-lilac) 55%, var(--art-tan) 100%);
    opacity: 0.75;
  }
  .brand-name {
    position: absolute; left: 0; right: 0; top: 208px;
    text-align: center;
    font-family: "Cinzel", serif; font-weight: 400;
    font-size: 27px; letter-spacing: 0.5px;
    color: var(--ink-violet);
  }
  .brand-tagline {
    position: absolute; left: 92px; right: 92px; top: 238px;
    display: flex; align-items: center; gap: 8px;
    font-family: "Arimo", sans-serif; font-weight: 700;
    font-size: 10px; letter-spacing: 0.4px;
    color: var(--ink-violet); white-space: nowrap;
  }
  .brand-tagline::before, .brand-tagline::after {
    content: ""; flex: 1; height: 1px; background: var(--ink-violet);
  }
  .holder-name {
    position: absolute; left: 0; right: 0; top: 130px;
    text-align: center;
    font-family: "Cinzel", serif; font-weight: 600;
    font-size: 23px; letter-spacing: 1px;
  }
  .mission {
    position: absolute; left: 110px; width: 252px; top: 194px;
    border-top: 1px solid var(--rule-soft);
    border-bottom: 1px solid var(--rule-soft);
    padding: 3px 0 4px;
    text-align: center;
    font-family: "Arimo", sans-serif; font-size: 12px; line-height: 14px;
    color: var(--text-soft);
  }
  .contact {
    position: absolute; left: 0; right: 0; top: 235px;
    display: flex; justify-content: center; align-items: center; gap: 6px;
    font-family: "Arimo", sans-serif; font-weight: 700; font-size: 13px;
  }
  .contact-item { display: flex; align-items: center; gap: 4px; }
  .contact-icon { width: 13px; height: 13px; }
</style>
</head>
<body>
  <main class="card">
    <section class="card-front">
      <div class="mascot-art" role="img" aria-label="Illustration of a winged pink unicorn beside a tan and white Cavalier King Charles spaniel with angel wings"></div>
      <div class="brand-name">STARLITMANES AND TAILS</div>
      <div class="brand-tagline">PET THERAPY ANIMALS</div>
    </section>
    <section class="card-back">
      <h1 class="holder-name">Rosalind Varga</h1>
      <p class="mission">Pet therapy animals give unconditional love<br>to the aged and disabled.</p>
      <div class="contact">
        <span class="contact-item">
          <svg class="contact-icon" viewBox="0 0 13 13" aria-hidden="true">
            <rect x="0.5" y="2" width="12" height="9" rx="2" fill="#ffffff"/>
            <path d="M2 4 L6.5 7.5 L11 4" fill="none" stroke="#535aa8" stroke-width="1.2"/>
          </svg>
          starlitmanesandtails@quellnet.com
        </span>
        <span class="contact-item">
          <svg class="contact-icon" viewBox="0 0 13 13" aria-hidden="true">
            <rect x="0.5" y="0.5" width="12" height="12" rx="2" fill="#ffffff"/>
            <path d="M4.5 3 C3 4.5 3 8.5 4.5 10 L6 9 L5.2 7.6 C4.8 6.8 4.8 6.2 5.2 5.4 L6 4 Z" fill="#535aa8"/>
          </svg>
          0417650382
        </span>
      </div>
    </section>
  </main>
</body>
</html>
```